Brochure for Pet Service

I need a brochure for my start up business. We personally deliver pet food to our customers door. Looking for a clean design communicating professionalism and trust to our customer.

Please visit our work in progress website at: www.brightpawcarriers.com to get a feel for what we offer.

Brochure should include the text from the 'About' page on our website: Listed Below.

Owning a pet is an amazing experience, but there is no denying that one of the least enjoyable aspects of pet ownership is driving to the store to buy pet food. No one wants make extra stops on their way to or from work and then to have to lug a 30 pound bag back to your car and eventually into your house. So why not simply eliminate all of that hassle?

Bright Paw is here to save you the time and effort and the best part is that we won’t charge you extra for the service. That’s right, free local delivery. We aren’t some big National company shipping your food via commercial transport, we are local, right here in the community. You don’t have to sign up for a contract or long term commitment, just give it a try and don’t look back.

Not only can we make getting pet products to your home and easy task, but we also aim to make it easier to select the perfect food for your pet. We don’t carry every brand on the market, but we feel confident that the brands we do have available will provide your pet some of the best in quality and nutrition. So take some time and read about what we carry and how it works and we hope to see you on our next delivery.

Should also include the 'How We Work' info:

Getting premium pet products delivered right to your door has never been easier. At Bright Paw, we strive to make one of the most inconvenient parts of pet ownership as hassle and worry free as possible. Order one bag at a time or sign-up for recurring deliveries. Here’s what to do.

1. Browse our extensive selection of premium pet products online and make your selection.

2. When you are done shopping, complete your transaction.

3. Sit back and let us do the rest.

Target Market(s)

Pet owners looking for convenience.

Industry/Entity Type

Shipping

Colors
f6f8fc

Requirements
Must have
• Bright Paw
www.BrightPawCarriers.com
Phone: 920-555-0173
Info@BrightPawCarriers.com

Photos of humans with dogs/cats.

Should not be dominated by bold colors. We want color, however, we don't want the base color to be a solid orange, blue, or green. We want bursts of colors to enhance the overall design. We do want our orange, blue, and green colors used in the overall design however.

Must have a place to stick a mailing address so we can send through the mail.
Nice to have
• Can use catch phrases such as:
Sit. Stay. Let us Fetch!
Making your life easier, theirs healthier and happier.
You can't buy happiness, but you can local and that's kinda the same thing.
Should not have
• Animated graphics, cats or dogs randomly placed without being included in an actual photo.

Our logo should not dominate any page. Should be visible throughout, however please don't plaster it as the only image on the cover.

```html
<!DOCTYPE html>
<html lang="en">
<head>
<meta charset="utf-8">
<title>Bright Paw – Brochure</title>
<link href="https://fonts.googleapis.com/css2?family=Arimo:wght@400&family=Open+Sans:wght@400;600;700&family=Dancing+Script:wght@500&display=swap" rel="stylesheet">
<style>
  :root{
    --page:#e6e7e9;
    --paper:#f6f8fc;
    --paper-mid:#e3e5e9;
    --ink:#1e1e1e;
    --muted:#6b6e72;
    --orange:#f08a1e;
    --green:#8dc63f;
    --blue:#3aa6dd;
  }
  *{box-sizing:border-box;margin:0;padding:0}
  html,body{width:1200px;height:998px;overflow:hidden;background:var(--page)}
  .brochure{position:absolute;left:70px;top:69px;width:1060px;height:860px;overflow:hidden;
    background:var(--paper);box-shadow:0 6px 24px rgba(0,0,0,.15)}
  .panel{position:absolute;top:0;height:100%;width:353px}
  .panel--left{left:0;background:var(--paper)}
  .panel--center{left:353px;width:354px;background:var(--paper-mid)}
  .panel--right{left:707px;background:var(--paper)}
  .body-copy{font-family:"Arimo",Arial,sans-serif;font-size:16px;line-height:19.5px;color:var(--ink);text-align:justify;position:absolute}
  .script{font-family:"Dancing Script",cursive;font-weight:500;position:absolute;line-height:1.3}
  .photo{position:absolute;border-radius:50%}
  .photo--top{left:320px;top:-20px;width:420px;height:230px;background:radial-gradient(ellipse at 40% 55%,#c9a27a 0%,#e9e3dc 45%,#f4f2ef 100%)}
  .photo--owner{left:5px;top:550px;width:340px;height:340px;background:radial-gradient(circle at 55% 45%,#d8b59c 0%,#7f9a55 45%,#3f6b2a 100%)}
  .photo--cat{left:725px;top:520px;width:340px;height:340px;background:radial-gradient(circle at 45% 45%,#8a7560 0%,#4a3e33 40%,#0f0d0b 100%)}
  .rings{position:absolute;left:0;top:0;width:1060px;height:860px;pointer-events:none}
  .brand{position:absolute;left:0;width:100%;top:250px;display:flex;justify-content:center;align-items:center;gap:12px}
  .brand__dot{width:34px;height:34px;border-radius:50%;background:var(--blue)}
  .brand__name{font-family:"Open Sans",sans-serif;font-weight:400;font-size:34px;color:var(--muted)}
  .contact{position:absolute;left:0;width:100%;font-family:"Open Sans",sans-serif;font-weight:600;font-size:17px;color:var(--ink);display:flex;justify-content:center;align-items:center;gap:8px}
  .contact--web{top:320px;font-size:18px;font-weight:700}
  .contact--mail{top:362px}
  .contact--phone{top:402px;font-size:18px}
  .contact svg{fill:#444}
</style>
</head>
<body>
<main class="brochure">
  <section class="panel panel--left">
    <p class="body-copy" style="left:28px;top:8px;width:270px">Owning a pet is an amazing experience, but there is no denying that one of the least enjoyable aspects of pet ownership is driving to the store to buy pet food. No one wants make extra stops on their way to or from work and then to have to lug a 30 pound bag back to your car and eventually into your house. So why not simply eliminate all of that hassle?</p>
    <p class="body-copy" style="left:28px;top:250px;width:305px">Bright Paw is here to save you the time and effort and the best part is that we won’t charge you extra for the service.</p>
    <p class="script" style="left:58px;top:340px;font-size:30px;color:var(--orange)">That’s right!<br>Free local delivery.</p>
    <svg class="arrow" style="position:absolute;left:170px;top:440px" width="130" height="90" viewBox="0 0 130 90" aria-hidden="true">
      <path d="M8 4 C 18 50, 55 72, 112 70" fill="none" stroke="var(--green)" stroke-width="5" stroke-linecap="round"/>
      <path d="M100 58 L116 70 L100 81" fill="none" stroke="var(--green)" stroke-width="5" stroke-linecap="round" stroke-linejoin="round"/>
    </svg>
  </section>

  <section class="panel panel--center">
    <div class="brand"><span class="brand__dot"></span><span class="brand__name">Bright Paw</span></div>
    <p class="contact contact--web">www.BrightPawCarriers.com</p>
    <p class="contact contact--mail">
      <svg width="24" height="16" viewBox="0 0 24 16" aria-hidden="true"><rect width="24" height="16" rx="1"/><path d="M1 1 L12 9 L23 1" fill="none" stroke="#e3e5e9" stroke-width="2"/></svg>
      Info@BrightPawCarriers.com</p>
    <p class="contact contact--phone">
      <svg width="20" height="20" viewBox="0 0 24 24" aria-hidden="true"><path d="M6.6 10.8a15.1 15.1 0 0 0 6.6 6.6l2.2-2.2c.3-.3.7-.4 1-.2 1.1.4 2.3.6 3.6.6.6 0 1 .4 1 1V20c0 .6-.4 1-1 1A17 17 0 0 1 3 4c0-.6.4-1 1-1h3.5c.6 0 1 .4 1 1 0 1.3.2 2.5.6 3.6.1.3 0 .7-.2 1z"/></svg>
      920-555-0173</p>
    <p class="body-copy" style="left:30px;top:518px;width:302px">We aren’t some big National company shipping your food via commercial transport, we are local, right here in the community. You don’t have to sign up for a contract or long term commitment.</p>
    <p class="script" style="left:75px;top:648px;font-size:30px;color:var(--green)">Just give it a try<br>and<br>don’t look back.</p>
  </section>

  <section class="panel panel--right">
    <p class="body-copy" style="left:55px;top:60px;width:270px;text-align:right">Not only can we make getting pet products to your home and easy task, but we also aim to make it easier to select the perfect food for your pet. We don’t carry every brand on the market, but we feel confident that the brands we do have available will provide your pet some of the best in quality and nutrition. So take some time and read about what we carry and how it works and ...</p>
    <p class="script" style="left:42px;top:345px;font-size:30px;color:var(--blue)">We hope to see you on<br>our next delivery.</p>
  </section>

  <div class="photo photo--top" role="img" aria-label="Photo of a dog and a cat eating from metal bowls"></div>
  <div class="photo photo--owner" role="img" aria-label="Photo of a smiling woman hugging a small terrier outdoors"></div>
  <div class="photo photo--cat" role="img" aria-label="Photo of a tabby cat licking its paw on a dark background"></div>

  <svg class="rings" viewBox="0 0 1060 860" aria-hidden="true" fill="none">
    <ellipse cx="530" cy="95" rx="214" ry="119" stroke="var(--green)" stroke-width="4"/>
    <ellipse cx="530" cy="95" rx="220" ry="125" stroke="var(--orange)" stroke-width="5"/>
    <ellipse cx="530" cy="95" rx="226" ry="131" stroke="var(--blue)" stroke-width="3"/>
    <circle cx="175" cy="720" r="175" stroke="var(--orange)" stroke-width="6"/>
    <circle cx="175" cy="720" r="182" stroke="var(--green)" stroke-width="4"/>
    <circle cx="175" cy="720" r="188" stroke="var(--blue)" stroke-width="3"/>
    <circle cx="895" cy="690" r="175" stroke="var(--orange)" stroke-width="6"/>
    <circle cx="895" cy="690" r="182" stroke="var(--green)" stroke-width="4"/>
    <circle cx="895" cy="690" r="188" stroke="var(--blue)" stroke-width="3"/>
  </svg>
</main>
</body>
</html>
```